Business Card Design Project

We need a Business Card for an Mechanical Engineering firm in Singapore. The design should be Modern & Technical looking, yet eye catching.

Our company deals in Cutting Tools & Machine Accessories for the Manufacturing Industries such as Oil & Gas, Aero Space, etc... For more information on our Company, you can either email me or view our website www.torvale.com.sg.

We are trying to revamp our image to give our consumers a fresh new perspective to our company, so we welcome all ideas.

Industry/Entity Type

Business

Requirements
Must have
• Must incorporate New Company Logo into the card as shown in Uploaded file.

```html
<!DOCTYPE html>
<html lang="en">
<head>
<meta charset="utf-8">
<title>Torvale Tools – Business Card</title>
<link rel="stylesheet" href="https://fonts.googleapis.com/css2?family=Arimo:wght@400;700&display=swap">
<style>
  :root {
    --backdrop: #ece9e4;
    --card: #ffffff;
    --maroon: #7c1a3c;
    --ink: #2b2b2b;
    --rule: #4a4a4a;
  }
  * { box-sizing: border-box; margin: 0; padding: 0; }
  html, body {
    width: 1200px;
    height: 798px;
    overflow: hidden;
    background: var(--backdrop);
    font-family: "Arimo", Arial, sans-serif;
  }
  .business-card {
    position: absolute;
    left: 150px;
    top: 139px;
    width: 900px;
    height: 520px;
    background: var(--card);
    border-radius: 44px;
    overflow: hidden;
    box-shadow: 0 6px 18px rgba(0,0,0,0.12);
  }
  .accent-tab {
    position: absolute;
    right: 0;
    top: 108px;
    width: 52px;
    height: 134px;
    background: var(--maroon);
  }
  .brand {
    position: absolute;
    left: 92px;
    top: 250px;
    display: flex;
    align-items: center;
    gap: 14px;
  }
  .brand-dot {
    width: 22px;
    height: 22px;
    border-radius: 50%;
    background: var(--maroon);
  }
  .brand-name {
    font-size: 34px;
    font-weight: 700;
    color: var(--maroon);
    letter-spacing: 1px;
  }
  .divider {
    position: absolute;
    left: 440px;
    top: 188px;
    width: 2px;
    height: 166px;
    background: var(--rule);
  }
  .contact {
    position: absolute;
    left: 476px;
    top: 196px;
    color: var(--ink);
    font-size: 19px;
    line-height: 25px;
  }
  .contact .company { font-weight: 700; }
  .contact .lines { margin-top: 26px; }
</style>
</head>
<body>
  <div class="business-card">
    <div class="accent-tab"></div>

    <div class="brand">
      <span class="brand-dot"></span>
      <span class="brand-name">TORVALE TOOLS</span>
    </div>

    <div class="divider"></div>

    <div class="contact">
      <p class="company">Torvale Tools Pte Ltd</p>
      <p>58 Kestrel Loop #03-12,</p>
      <p>Norden Business Park,</p>
      <p>Singapore 129642.</p>
      <div class="lines">
        <p>Tel: 65-61234570 | Fax: 65-61234571</p>
        <p>Email: hello@torvale.com.sg</p>
      </div>
    </div>
  </div>
</body>
</html>
```